DEIJ Annual Progress Report

We need a Word-based year-end progress report for The Calloway Partners, Inc. for their client Brookvale Care Network. The report should be easily editable because this report represents the first draft. We want the report to use The Calloway Partners, Inc.'s colors as the main color and incorporate the client's colors as ascents. Please provide two spots per page where photos can be inserted.
Updates

Please include an introduction and conclusion paragraph. I will add that text later.

I uploaded the introduction and conclusion to use with the report.

Give some designer a chance to response, or update their designs.

Target Market(s)

Healthcare Executives

Industry/Entity Type

Healthcare consulting

Font styles to use
Other font styles liked:
• Loto, and Raleway

Requirements
Must have
• Use of the TCP and BVCN logos, appropriate photos in case I go with stock photos
Nice to have
• Warm but professional feeling
Should not have
• Cartoons, silly or funny pictures

```html
<!DOCTYPE html>
<html lang="en">
<head>
<meta charset="utf-8">
<title>TCP BVCN 2023 Progress Summary</title>
<link rel="stylesheet" href="https://fonts.googleapis.com/css2?family=Lato:wght@300;400;700;900&display=swap">
<style>
  :root {
    --navy: #2a2563;
    --navy-deep: #221e55;
    --gold: #a8822f;
    --magenta: #d6288f;
    --ink: #4a4a4a;
    --stage: #eef1f4;
    --paper: #ffffff;
    --photo-a: #b9d4ea;
    --photo-b: #9cc77a;
  }
  * { box-sizing: border-box; margin: 0; padding: 0; }
  html, body { width: 1200px; height: 944px; overflow: hidden; background: var(--stage); }
  body { font-family: "Lato", Arial, sans-serif; color: var(--ink); }

  .board {
    position: absolute; left: 0; top: 0;
    width: 2172px; height: 1708px;
    transform: scale(0.5525); transform-origin: 0 0;
  }
  .page {
    position: absolute; width: 363px; height: 514px;
    background: var(--paper); overflow: hidden;
  }
  .page::before, .page::after {
    content: ""; position: absolute; left: 0; right: 0; height: 14px;
    background: linear-gradient(var(--navy) 0 5px, var(--gold) 5px 9px, var(--paper) 9px 10px, var(--navy) 10px 14px);
  }
  .page::before { top: 0; }
  .page::after { bottom: 0; transform: scaleY(-1); }

  .running-head { position: absolute; top: 22px; left: 0; right: 0; text-align: center; }
  .running-head .report-title { font-size: 6.6px; font-weight: 900; color: #222; }
  .running-head .report-sub { font-size: 5.6px; font-weight: 300; color: #555; }

  .page-body { position: absolute; top: 48px; left: 55px; right: 55px; font-size: 6px; line-height: 1.22; }
  .page-body p { text-align: justify; margin-bottom: 7px; }
  .folio { position: absolute; bottom: 22px; left: 0; right: 0; text-align: center; font-size: 4px; color: #777; }

  .section-title { font-size: 10px; font-weight: 900; color: var(--navy); margin: 4px 0 2px; }
  .item-title { font-size: 8.4px; font-weight: 700; color: var(--navy); }
  .lead { font-weight: 700; color: var(--navy); font-size: 7.6px; }

  .dot-list, .diamond-list { list-style: none; }
  .dot-list > li { position: relative; padding-left: 13px; margin-bottom: 4px; }
  .dot-list > li::before { content: "●"; position: absolute; left: 1px; top: 1px; font-size: 6px; color: var(--navy); }
  .diamond-list { margin: 1px 0 2px 16px; }
  .diamond-list > li { position: relative; padding-left: 11px; margin-bottom: 2px; text-align: justify; }
  .diamond-list > li::before { content: "❖"; position: absolute; left: 0; top: 0; font-size: 5.6px; color: #333; }
  .flush { margin-left: 0; }

  .photo-slot {
    display: block; width: 66px; height: 72px; margin: 8px 0 10px 46px;
    border-radius: 4px; border: 3px solid #fff;
    background: linear-gradient(160deg, var(--photo-a) 0 55%, var(--photo-b) 55% 100%);
    box-shadow: 0 0 0 1px #dbe7f0;
  }

  .client-name { display: flex; align-items: center; justify-content: center; gap: 5px; margin: 4px 0 8px; font-weight: 900; color: var(--navy); font-size: 9px; line-height: 1.05; }
  .client-name .mark-square { width: 9px; height: 9px; background: var(--magenta); flex: none; }

  .partner-name { display: flex; align-items: center; justify-content: center; gap: 8px; margin-top: 28px; font-weight: 900; color: var(--navy); font-size: 17px; line-height: 1.05; }
  .partner-name .mark-circle { width: 30px; height: 30px; border-radius: 50%; background: var(--gold); flex: none; }

  /* cover */
  .cover::before, .cover::after { display: none; }
  .cover svg { position: absolute; inset: 0; }
  .cover-brands { position: absolute; top: 22px; left: 112px; right: 12px; display: flex; align-items: center; gap: 12px; color: var(--navy); font-weight: 900; }
  .cover-brands .client { font-size: 10px; line-height: 1.05; display: flex; align-items: center; gap: 4px; }
  .cover-brands .client .mark-square { width: 9px; height: 9px; background: var(--magenta); flex: none; }
  .cover-brands .partner { font-size: 13px; line-height: 1.05; display: flex; align-items: center; gap: 6px; }
  .cover-brands .partner .mark-circle { width: 22px; height: 22px; border-radius: 50%; background: var(--gold); flex: none; }
  .cover-title { position: absolute; left: 145px; top: 400px; color: #fff; font-weight: 900; font-size: 19px; line-height: 1.2; }
  .cover-title .accent { color: var(--magenta); }
</style>
</head>
<body>
<div class="board">

  <!-- Cover -->
  <section class="page cover" style="left:79px;top:66px">
    <svg width="363" height="514" viewBox="0 0 363 514">
      <polygon points="0,0 55,0 178,168 363,168 363,514 0,514" fill="var(--navy-deep)"/>
      <polygon points="0,334 150,334 56,430 56,514 0,514" fill="var(--gold)"/>
      <polygon points="186,172 286,172 336,275 286,378 186,378 136,275" fill="#fff"/>
      <defs>
        <linearGradient id="photoTone" x1="0" y1="0" x2="1" y2="1">
          <stop offset="0" stop-color="#e7e4df"/>
          <stop offset="0.5" stop-color="#b08a6c"/>
          <stop offset="1" stop-color="#d9d5cf"/>
        </linearGradient>
      </defs>
      <polygon role="img" aria-label="Photo: diverse team joining hands in a circle" points="190,180 282,180 328,275 282,370 190,370 144,275" fill="url(#photoTone)"/>
    </svg>
    <div class="cover-brands">
      <div class="client"><span class="mark-square"></span><span>Brookvale<br>Care<br>Network</span></div>
      <div class="partner"><span class="mark-circle"></span><span>The Calloway<br>Partners, Inc.</span></div>
    </div>
    <h1 class="cover-title">TCP <span class="accent">BVCN</span> 2023<br>Progress Summary</h1>
  </section>

  <!-- Page 2: Introduction -->
  <section class="page" style="left:491px;top:66px">
    <header class="running-head"><div class="report-title">The Calloway Partners, Inc. Backbone Support 2023 Progress Report</div><div class="report-sub">Driving Anti-Racism Strategy at Brookvale Care Network</div></header>
    <div class="page-body">
      <h2 class="section-title">Introduction:</h2>
      <p>The Calloway Partners, Inc., a Black woman-owned global diversity, equity, inclusion, and justice (DEIJ) consulting firm established in 1984, brings over 80 years of combined experience in its field. Specializing in learning and education, cultural audits, and strategy development, the firm is dedicated to centering its work on those most impacted by injustice and oppression. Through advancing DEIJ thought leadership and partnering with committed organizations, The Calloway Partners strives to build equitable and just systems within workplaces and beyond.</p>
      <p>Our collaboration with Brookvale Care Network (BVCN)</p>
      <div class="client-name"><span class="mark-square"></span><span>Brookvale<br>Care Network</span></div>
      <p>focused on providing Backbone Support for their Anti-Racism Road Map, has been a source of both honor and pleasure. This partnership aims to enhance BVCN's capacity to deliver exceptional patient care in diverse communities, fostering an anti-racist and equitable healthcare environment that actively confronts all forms of racism while promoting greater diversity, inclusion, and equity among its workforce and those it serves.</p>
      <p>This report outlines The Calloway Partners' role, achievements, and contributions to BVCN in 2023 and presents forward-looking recommendations to further advance the Equity and Anti-Racism Road map.</p>
      <p>Throughout 2023, The Calloway Partners, Inc. has achieved significant milestones in collaboration with Brookvale Care Network (BVCN). Notably, we successfully facilitated the development and implementation of comprehensive DEIJ strategies, which included the integration of a learning journey within the leadership model and the effective alignment of various strategic initiatives under the Anti Racism Road Map. Our efforts in conducting cultural audits and enhancing operational efficiencies have been instrumental in advancing BVCN's commitment to equity and inclusion.</p>
      <p>Looking ahead, this report will unveil insightful recommendations that build upon these accomplishments. We propose strategic initiatives that not only consolidate our past successes but also chart a path forward for</p>
    </div>
    <div class="folio">2</div>
  </section>

  <!-- Page 3: Conclusion -->
  <section class="page" style="left:904px;top:66px">
    <header class="running-head"><div class="report-title">The Calloway Partners, Inc. Backbone Support 2023 Progress Report</div><div class="report-sub">Driving Anti-Racism Strategy at Brookvale Care Network</div></header>
    <div class="page-body">
      <p>sustained impact. These recommendations are designed to deepen BVCN's commitment to anti-racism, broaden its scope to embrace intersectionality, and further integrate patient and community voices into its framework. We believe that the implementation of these recommendations will be pivotal in elevating BVCN's position as a leader in equitable healthcare delivery. We invite you to explore the detailed insights and strategic directions outlined in the subsequent sections of this report."</p>
      <h2 class="section-title">Conclusion:</h2>
      <p>As we conclude this progress report, The Calloway Partners, Inc. wishes to express our profound gratitude for the opportunity to collaborate with Brookvale Care Network (BVCN). This partnership has not only been a journey of implementing meaningful change but also a testament to the commitment and dedication of both our organizations towards fostering a more equitable and inclusive healthcare environment.</p>
      <div class="partner-name"><span class="mark-circle"></span><span>The Calloway<br>Partners, Inc.</span></div>
    </div>
    <div class="folio">3</div>
  </section>

  <!-- Page 4: Partnership & Progress -->
  <section class="page" style="left:1317px;top:66px">
    <header class="running-head"><div class="report-title">The Calloway Partners, Inc. Backbone Support 2023 Progress Report</div><div class="report-sub">Driving Anti-Racism Strategy at Brookvale Care Network</div></header>
    <div class="page-body" style="top:54px">
      <h2 class="section-title">Partnership:</h2>
      <ul class="dot-list">
        <li><span class="item-title">The Partnership Overview</span>
          <ul class="diamond-list"><li>Partnership initiation: February 2022</li><li>Purpose: Implementing the Anti-Racism Road Map</li><li>Backbone Support within the Collective Impact Model</li></ul></li>
        <li><span class="item-title">Project Key Assumptions</span>
          <ul class="diamond-list"><li>Collective Impact Model guides strategy implementation</li><li>Emphasis on change management and theories of change</li><li>Commitment from BVCN to prioritize and resource the initiative.</li></ul></li>
        <li><span class="item-title">The Role of The Calloway Partners, Inc.</span>
          <ul class="diamond-list"><li>Providing Backbone Support as per the Collective Impact Model</li><li>Developing a sustainable strategic architecture</li><li>Supporting the establishment of working teams and providing consultative support</li></ul></li>
      </ul>
      <h2 class="section-title">Progress:</h2>
      <ul class="dot-list">
        <li><span class="item-title">Guiding Vision and Strategy</span>
          <ul class="diamond-list"><li>Facilitated the development of four synergistic goals derived from 11 strategies.</li><li>Spearheaded EDLB, PI, and Strategy Lead presentations to track progress and set objectives.</li><li>Played a pivotal role in shaping goals and defining measures of success</li></ul>
          <span class="photo-slot" role="img" aria-label="Photo placeholder"></span>
          <ul class="diamond-list"><li>EDLB presentations and Strategy Leads' testimonials confirm the guidance.</li></ul></li>
        <li><span class="item-title">Supporting Aligned Activities</span>
          <ul class="diamond-list"><li>Coaches worked closely with strategy leads to define actions for strategy advancement.</li></ul></li>
      </ul>
    </div>
    <div class="folio">4</div>
  </section>

  <!-- Page 5 -->
  <section class="page" style="left:1730px;top:66px">
    <header class="running-head"><div class="report-title">The Calloway Partners, Inc. Backbone Support 2023 Progress Report</div><div class="report-sub">Driving Anti-Racism Strategy at Brookvale Care Network</div></header>
    <div class="page-body">
      <ul class="dot-list">
        <li style="padding-left:0">
          <ul class="diamond-list"><li>Developed a coaching template integrating a learning journey within the BVCN leadership model.</li><li>Ensured alignment and synergy among Strategies Leads to further collective goals.</li></ul>
          <span class="photo-slot" role="img" aria-label="Photo placeholder"></span>
          <ul class="diamond-list"><li>documentation of the learning journey's integration with the leadership model and examples of the coaching template.</li></ul></li>
        <li><span class="item-title">Establishing Shared Measurement Practices</span>
          <ul class="diamond-list"><li>Led the creation of four overarching goals aligning with 11 strategies.</li><li>Initiated the development of success objectives and their transformation into measurable indicators.</li><li>Took charge of establishing shared goals and the methodology for measuring success.</li></ul>
          <span class="photo-slot" role="img" aria-label="Photo placeholder"></span>
          <ul class="diamond-list"><li>The actual goals and objectives documents that illustrate the use of shared data in decision-making processes.</li></ul></li>
        <li><span class="item-title">Building Public Will</span>
          <ul class="diamond-list"><li>Proposed and participated in the D&amp;I Summit, with our CEO as a key speaker.</li><li>Actively participated in executive diversity leadership boards (EDLB) meetings.</li></ul></li>
      </ul>
    </div>
    <div class="folio">5</div>
  </section>

  <!-- Page 6 -->
  <section class="page" style="left:79px;top:598px">
    <header class="running-head"><div class="report-title">The Calloway Partners, Inc. Backbone Support 2023 Progress Report</div><div class="report-sub">Driving Anti-Racism Strategy at Brookvale Care Network</div></header>
    <div class="page-body">
      <ul class="dot-list">
        <li style="padding-left:0">
          <ul class="diamond-list flush"><li>Participated in internal and potential external support through annual reports and publications.</li></ul>
          <span class="photo-slot" role="img" aria-label="Photo placeholder"></span>
          <ul class="diamond-list"><li>Event agendas and recordings, feedback surveys from the D&amp;I Summit, communication materials such as newsletters or annual reports, and media coverage of public engagements.</li></ul></li>
        <li><span class="item-title">Fostering Continuous Learning and Development</span>
          <ul class="diamond-list"><li>Integrated coaching with the existing leadership model, adding depth with a focus on anti-racist leadership.</li><li>Embedded wellness and resilience-building within strategic development.</li><li>The Calloway Partners, Inc. CEO was actively involved in providing continuous learning.</li></ul>
          <span class="photo-slot" role="img" aria-label="Photo placeholder"></span>
          <ul class="diamond-list"><li>Descriptions of the leadership model enhancements, training materials, participant feedback on learning and development programs, and case studies of how the learning has been applied.</li></ul></li>
        <li><span class="item-title">Mobilizing Funding</span>
          <ul class="diamond-list"><li>While not directly involved in funding, we've laid the groundwork for financial validation.</li><li>Articulated clear goals, success objectives, and measurable outcomes to support funding efforts.</li><li>Preparing to benchmark progress on the measures suggested to attract sustainable resources.</li></ul></li>
      </ul>
    </div>
    <div class="folio">6</div>
  </section>

  <!-- Page 7: Next Steps -->
  <section class="page" style="left:491px;top:598px">
    <header class="running-head"><div class="report-title">The Calloway Partners, Inc. Backbone Support 2023 Progress Report</div><div class="report-sub">Driving Anti-Racism Strategy at Brookvale Care Network</div></header>
    <div class="page-body">
      <div class="lead">Next Steps</div>
      <h2 class="section-title">Governance:</h2>
      <ul class="dot-list">
        <li><span class="lead">Reflective Review of the Roadmap's Focus:</span> Assess the need to adjust mission, operational planning, and membership based on recent developments, learning's, and participant feedback.
          <ul class="diamond-list" style="margin-top:6px">
            <li><span class="lead">Broadening Anti-Racism Efforts:</span> Address intersectionality by actively reducing not just racism but also related forms of discrimination such as Antisemitism, Islamophobia, and Anti-Transgender Attitudes.</li>
            <li><span class="lead">Operational Alignment:</span> Continue to assess and adjust the Roadmap's governance structure based on recent developments and feedback. Ensure that governance is closely aligned with the evolving goals and strategies of the Roadmap.</li>
            <li><span class="lead">Commitment and Support Structures:</span> Reinforce the commitment from all Brookvale Care Network levels to the Roadmap. Develop support structures that facilitate staff's active participation and contribution at various levels.</li>
            <li><span class="lead">Enhanced Operational Communication:</span> Implement robust internal communication strategies to inform all stakeholders about the Roadmap's progress, changes, and expectations. This helps in maintaining transparency and building trust among the team members.</li>
            <li><span class="lead">Training and Development for Operational Staff:</span> Provide targeted training and development programs for staff involved in the operational aspects of the Roadmap. This ensures they have the necessary skills and knowledge to effectively contribute to the initiative.</li>
          </ul></li>
      </ul>
      <h2 class="section-title" style="margin-top:8px">Strategy</h2>
      <ul class="diamond-list" style="margin-left:6px">
        <li style="padding-left:0"><span class="lead">Funding Mobilization:</span> Strategic plans highlighting the long-term funding strategy, documents showing how the goals align with funding requirements, and pre-and post-measures of the impact of funding on the initiative's success.</li>
        <li><span class="lead">Sustainability and Anti-Racism Synergy:</span> Ensure sustainability efforts are infused with anti-racism principles, creating long-lasting systemic change.</li>
      </ul>
    </div>
    <div class="folio">7</div>
  </section>

  <!-- Page 8: Policy & Learning -->
  <section class="page" style="left:904px;top:598px">
    <header class="running-head"><div class="report-title">The Calloway Partners, Inc. Backbone Support 2023 Progress Report</div><div class="report-sub">Driving Anti-Racism Strategy at Brookvale Care Network</div></header>
    <div class="page-body">
      <ul class="diamond-list">
        <li><span class="lead">Policy Review with Equity in Focus:</span> Analyze Medicaid reimbursement policies through an equity lens to identify and challenge systemic biases.</li>
        <li><span class="lead">Advocacy for Equitable Practices:</span> Drive advocacy initiatives to rectify disparities in reimbursement rates, championing fair treatment across all communities.</li>
        <li><span class="lead">Data Transparency for Accountability:</span> Implement robust reporting mechanisms to track progress against anti-racism goals and facilitate accountability transparently.</li>
        <li><span class="lead">Collaborative Efforts Against Racial Inequities:</span> Forge and reinforce partnerships dedicated to addressing healthcare disparities resulting from racial inequity.</li>
      </ul>
      <h2 class="section-title" style="margin-top:8px">Learning:</h2>
      <ul class="diamond-list">
        <li><span class="lead">Tailored Education Programs:</span> Develop and implement training programs tailored to the needs of BVCN staff at all levels to deepen their understanding of anti-racism, intersectionality, and healthcare equity.</li>
        <li><span class="lead">Regular Workshops on Policy and Advocacy:</span> Conduct workshops to educate and empower staff on the nuances of Medicaid policy, advocacy techniques, and the importance of equity-focused reform.</li>
        <li><span class="lead">Knowledge Sharing Forums:</span> Establish regular forums where team members can share insights and best practices and learn from the experiences of others within the initiative.</li>
        <li><span class="lead">Cultural Competency Training:</span> Enhance cultural competency across the organization through specialized training sessions that address the various forms of discrimination identified in the Roadmap.</li>
        <li style="margin-top:8px"><span class="lead">Research Dissemination:</span> Facilitate sessions to disseminate and discuss current research findings on racial inequities in healthcare and Medicaid reimbursements.</li>
        <li><span class="lead">Feedback Mechanisms for Continuous Learning:</span> Create channels for continuous feedback on the Roadmap's implementation, allowing for real-time learning and immediate application of new insights.</li>
      </ul>
    </div>
    <div class="folio">8</div>
  </section>

  <!-- Page 9: Backbone Focus in 2024 -->
  <section class="page" style="left:1317px;top:598px">
    <header class="running-head"><div class="report-title">The Calloway Partners, Inc. Backbone Support 2023 Progress Report</div><div class="report-sub">Driving Anti-Racism Strategy at Brookvale Care Network</div></header>
    <div class="page-body">
      <h2 class="section-title">Backbone Focus in 2024</h2>
      <ul class="diamond-list">
        <li><span class="lead">Medicaid Impact Analysis:</span> Deepen understanding of how Medicaid affects healthcare equity to identify areas needing reform and why it's crucial for fair healthcare access.</li>
        <li><span class="lead">Policy Advocacy:</span> Support changes in reimbursement policies to ensure equitable practices, underlining the importance of systemic equity in healthcare financing.</li>
        <li><span class="lead">Ongoing Research and Monitoring:</span> Continue research to shape informed strategies and measure the impact of initiatives, highlighting the importance of evidence-based decision-making.</li>
        <li><span class="lead">Cultural Competency Training:</span> Enhance training in healthcare settings to address biases, emphasizing the need for an inclusive healthcare environment that respects diverse patient backgrounds.</li>
        <li><span class="lead">Educational Support for Strategic Goals:</span> Ensure that learning initiatives reinforce key organizational functions—critical for maintaining an informed, responsive, and proactive governance structure.</li>
        <li><span class="lead">Intersectional Anti-Racism Approach:</span> Expand efforts to explicitly address intersectionality within anti-racism work, acknowledging the complex interplay of various forms of discrimination and their impact on individuals and communities.</li>
      </ul>
      <h2 class="section-title" style="margin-top:12px">Recommendations:</h2>
      <ul class="dot-list">
        <li><span class="item-title">Update Roadmap Mission:</span>
          <ul class="diamond-list">
            <li><span class="lead">Connect Equity and Anti-Racism to Sustainability:</span> Demonstrate how integrating equity and anti-racism strategies can enhance organizational sustainability by potentially lowering costs, increasing funding, and improving operational efficiency.</li>
            <li><span class="lead">Broaden Focus to Intersectionality:</span> Expand the Anti-Racism Road Map to explicitly include intersectionality, addressing the interconnected nature of racism with other forms of discrimination such as Antisemitism, Islamophobia, and Anti-Transgender Attitudes.</li>
          </ul></li>
      </ul>
    </div>
    <div class="folio">9</div>
  </section>

  <!-- Page 10 -->
  <section class="page" style="left:1730px;top:598px">
    <header class="running-head"><div class="report-title">The Calloway Partners, Inc. Backbone Support 2023 Progress Report</div><div class="report-sub">Driving Anti-Racism Strategy at Brookvale Care Network</div></header>
    <div class="page-body">
      <ul class="dot-list">
        <li><span class="item-title">Integrate Patient and Community Voices:</span>
          <ul class="diamond-list"><li><span class="lead">Incorporate Diverse Perspectives:</span> Enhance the Roadmap by actively involving patients and community members, especially from marginalized groups, in the planning and implementation phases. This approach ensures that the initiatives are responsive to the real needs and experiences of those most impacted by healthcare disparities.</li></ul></li>
        <li><span class="item-title">Streamline Efforts:</span>
          <ul class="diamond-list"><li><span class="lead">Efficiency and Impact Optimization:</span> Examine the Roadmap for potential overlapping strategies or duplicities. Streamline these efforts to optimize resource utilization and amplify the initiative's impact.</li></ul></li>
        <li><span class="item-title">Enhance Educational Initiatives:</span>
          <ul class="diamond-list"><li><span class="lead">Targeted Learning Programs:</span> Develop and refine educational programs that are tailored to the evolving needs of BVCN staff, with a focus on deepening their understanding of anti-racism, intersectionality, and healthcare equity.</li><li><span class="lead">Support for Strategic Goals:</span> Align learning initiatives with strategic goals to reinforce key organizational functions, ensuring an informed, responsive, and proactive governance structure.</li></ul></li>
        <li><span class="item-title">Advocacy and Policy Engagement:</span>
          <ul class="diamond-list"><li><span class="lead">Reinforce Advocacy for Equity:</span> Continue to advocate for policy changes, particularly in Medicaid reimbursements, to align with equitable practices. Emphasize the systemic importance of equity in healthcare financing.</li><li><span class="lead">Policy Review and Adaptation:</span> Keep up the momentum in reviewing and adapting policies through an equity lens, ensuring the healthcare system remains fair and inclusive.</li></ul></li>
        <li><span class="item-title">Ongoing Research and Adaptive Strategies:</span>
          <ul class="diamond-list"><li><span class="lead">Sustained Research Efforts:</span> Maintain a strong focus on research and long-term monitoring to inform and adapt strategies as needed, emphasizing the importance of evidence-based decision-making.</li><li><span class="lead">Responsive and Dynamic Approach:</span> Stay agile and responsive to changes in the healthcare landscape, ensuring that Brookvale Care Network continues to innovate and adapt for future success.</li></ul></li>
      </ul>
    </div>
    <div class="folio">10</div>
  </section>

  <!-- Page 11 -->
  <section class="page" style="left:79px;top:1128px">
    <header class="running-head"><div class="report-title">The Calloway Partners, Inc. Backbone Support 2023 Progress Report</div><div class="report-sub">Driving Anti-Racism Strategy at Brookvale Care Network</div></header>
    <div class="page-body">
      <ul class="diamond-list">
        <li><span class="lead">Policy Review with Equity in Focus:</span> Analyze Medicaid reimbursement policies through an equity lens to identify and challenge systemic biases.</li>
        <li><span class="lead">Advocacy for Equitable Practices:</span> Drive advocacy initiatives to rectify disparities in reimbursement rates, championing fair treatment across all communities.</li>
        <li><span class="lead">Data Transparency for Accountability:</span> Implement robust reporting mechanisms to track progress against anti-racism goals and facilitate accountability transparently.</li>
        <li><span class="lead">Collaborative Efforts Against Racial Inequities:</span> Forge and reinforce partnerships dedicated to addressing healthcare disparities resulting from racial inequity.</li>
      </ul>
      <h2 class="section-title" style="margin-top:8px">Learning:</h2>
      <ul class="diamond-list">
        <li><span class="lead">Tailored Education Programs:</span> Develop and implement training programs tailored to the needs of BVCN staff at all levels to deepen their understanding of anti-racism, intersectionality, and healthcare equity.</li>
        <li><span class="lead">Regular Workshops on Policy and Advocacy:</span> Conduct workshops to educate and empower staff on the nuances of Medicaid policy, advocacy techniques, and the importance of equity-focused reform.</li>
        <li><span class="lead">Knowledge Sharing Forums:</span> Establish regular forums where team members can share insights and best practices and learn from the experiences of others within the initiative.</li>
        <li><span class="lead">Cultural Competency Training:</span> Enhance cultural competency across the organization through specialized training sessions that address the various forms of discrimination identified in the Roadmap.</li>
        <li style="margin-top:8px"><span class="lead">Research Dissemination:</span> Facilitate sessions to disseminate and discuss current research findings on racial inequities in healthcare and Medicaid reimbursements.</li>
        <li><span class="lead">Feedback Mechanisms for Continuous Learning:</span> Create channels for continuous feedback on the Roadmap's implementation, allowing for real-time learning and immediate application of new insights.</li>
      </ul>
    </div>
    <div class="folio">11</div>
  </section>

</div>
</body>
</html>
```